Flyer Design Project

To whom it may concern
Would love the benefit of your expertise

I have a project which is to increase business activity. There are dozens or real estate adds and I want mine to stand out from all others.

My strategy is going with a 50 % sale, what I need is something catchy and something that will make my brochure stand out from the other dozen brochure they have in the mail I need the WOW! Factor

DL Brochure (DL Brochures, Size 99 mm X 210 mm) atm the moment im thinking of only using 1 side but if your design needs both side that is an option

below will be the wording I'm thinking of going with the describe the sale and benefits, i am flexible with the wording if your think something else will sound better

***New Wording***

50% OFF COMMISSION
Sounds good doesn’t it?
Our promise to you from Harlow Real Estate

List your property with us
And if your buyer has not been found within 15 days
We will slash 50% off our commission!
You will have the benefit of Real Estate consultants
Derek Harlow and Anthony Velluti
With over 40 years combined experience
Working hard to find your buyer.

Call Today 0491 627 158

Condition Apply

Follow us on Facebook www.facebook.com/kelbrookhomes

I have attached the link to our website and Facebook page if you want to see a possible color scheme
but i am open to anything

http://keystonekelbrook.com.au/
http://www.facebook.com/kelbrookhomes

Good Luck !!!

Target Market(s)

Home Seller's

Industry/Entity Type

Real Estate

Requirements
Nice to have
• our logo but remember this flyer is not to market our self its to market our offer
so i want to 50% off the stand out not Keystone Harlow Real Estate
Should not have
• House in the Background, i would much rather the 50% take up half the page than have the house or even a quirky un related image

```html
<!DOCTYPE html>
<html lang="en">
<head>
<meta charset="utf-8">
<title>50% Off Commission – Harlow Real Estate</title>
<link href="https://fonts.googleapis.com/css2?family=Roboto:wght@300;400&display=swap" rel="stylesheet">
<style>
  :root {
    --frame: #e6e7e8;
    --paper: #ffffff;
    --red: #d2343a;
    --salmon: #e6907a;
    --maroon: #8e2a2e;
    --ink: #1d1d1b;
    --rule-grey: #d6d7d9;
  }
  html, body {
    margin: 0;
    padding: 0;
    overflow: hidden;
  }
  body {
    width: 1200px;
    height: 2438px;
    background: var(--frame);
    font-family: "Roboto", Arial, sans-serif;
    position: relative;
  }
  .flyer {
    position: absolute;
    left: 57px;
    top: 57px;
    width: 1089px;
    height: 2330px;
    background: var(--paper);
    overflow: hidden;
  }
  .hero-photo {
    position: absolute;
    left: 0;
    top: 0;
    width: 1089px;
    height: 1153px;
    background: linear-gradient(180deg,
      #cfd2d3 0%, #c9c7c0 18%, #cdbba1 38%, #bfa37f 58%, #a78f72 72%, #6f8a4c 86%, #5f7d3f 100%);
  }
  .offer-box {
    position: absolute;
    left: 75px;
    top: 848px;
    width: 930px;
    height: 295px;
    background: var(--red);
    color: var(--paper);
    text-align: center;
  }
  .offer-headline {
    margin: 0;
    padding-top: 56px;
    font-weight: 300;
    font-size: 150px;
    line-height: 1;
    letter-spacing: 1px;
  }
  .offer-sub {
    margin: 6px 0 0;
    font-weight: 300;
    font-size: 64px;
    line-height: 1;
    letter-spacing: 1px;
  }
  .promise-box {
    position: absolute;
    left: 75px;
    top: 1143px;
    width: 930px;
    height: 176px;
    background: var(--salmon);
    color: var(--paper);
    text-align: center;
    font-weight: 300;
    font-size: 37px;
    line-height: 50px;
    padding-top: 38px;
    box-sizing: border-box;
  }
  .promise-box p { margin: 0; }
  .offer-details {
    position: absolute;
    left: 106px;
    top: 1390px;
    margin: 0;
    color: var(--ink);
    font-weight: 400;
    font-size: 37px;
    line-height: 41px;
  }
  .call-label {
    position: absolute;
    left: 106px;
    top: 1748px;
    margin: 0;
    color: var(--ink);
    font-weight: 300;
    font-size: 64px;
    line-height: 1;
  }
  .call-number {
    position: absolute;
    left: 106px;
    top: 1832px;
    margin: 0;
    color: var(--ink);
    font-weight: 300;
    font-size: 90px;
    line-height: 1;
  }
  .conditions {
    position: absolute;
    left: 106px;
    top: 2068px;
    margin: 0;
    color: var(--ink);
    font-weight: 400;
    font-size: 35px;
  }
  .footer-shapes {
    position: absolute;
    left: 0;
    top: 0;
    width: 1089px;
    height: 2330px;
  }
  .social {
    position: absolute;
    left: 725px;
    top: 2199px;
    display: flex;
    align-items: center;
    gap: 26px;
    color: var(--paper);
    font-weight: 400;
    font-size: 32px;
  }
  .social-square {
    width: 56px;
    height: 56px;
    background: #3b5a9a;
  }
</style>
</head>
<body>
  <main class="flyer">
    <div class="hero-photo" role="img" aria-label="Photograph of a two-storey brick and weatherboard home with a double garage, potted palms and a front lawn"></div>

    <section class="offer-box">
      <h1 class="offer-headline">50% OFF</h1>
      <p class="offer-sub">COMMISSION</p>
    </section>

    <section class="promise-box">
      <p>Sounds good doesn’t it?</p>
      <p>Our promise to you from Harlow Real Estate</p>
    </section>

    <p class="offer-details">
      List your property with us<br>
      And if your buyer has not been found within 15 days<br>
      We will slash 50% off our commission!<br>
      You will have the benefit of Real Estate consultants<br>
      Derek Harlow and Anthony Velluti<br>
      With over 40 years combined experience<br>
      Working hard to find your buyer.
    </p>

    <p class="call-label">Call Today</p>
    <p class="call-number">0491 627 158</p>

    <p class="conditions">Condition Apply</p>

    <svg class="footer-shapes" viewBox="0 0 1089 2330" aria-hidden="true">
      <polygon points="0,2330 880,2172 900,2185 170,2330" fill="var(--rule-grey)"/>
      <polygon points="500,2175 1089,1980 1089,2330 250,2330" fill="var(--red)"/>
      <polygon points="830,2065 1089,1980 1089,2020 900,2080" fill="var(--maroon)"/>
    </svg>

    <div class="social">
      <span class="social-name">kelbrookhomes</span>
      <span class="social-square"></span>
    </div>
  </main>
</body>
</html>
```